Rivet Athletic Supply Inc.

Need to create a website that is informational and has the ability to sell goods and services. Such as a custom t shirt designer where the user can upload and image to be displayed on the garmet. The sports we specialize in are basketball, football, and baseball.

Would like like:
Home Page
Locker Room Page:
Custom Uniforms Page
Custom Shirt Creator
Brands
About

Competitor websites are
lornfieldsportsco.example
qtv.example
wmdgear.example

```html
<!DOCTYPE html>
<html lang="en">
<head>
<meta charset="utf-8">
<title>Rivet Athletic Supply — Custom Sports Apparel</title>
<link href="https://fonts.googleapis.com/css2?family=Poppins:ital,wght@0,400;0,500;0,600;0,700;0,800;1,600&display=swap" rel="stylesheet">
<style>
:root{
  --blue:#2a5cae;
  --blue-dark:#244f98;
  --red:#d63d3a;
  --ink:#222;
  --grey:#f2f2f3;
  --line:#e3e3e3;
  --white:#fff;
}
*{box-sizing:border-box;margin:0;padding:0}
html,body{width:1200px;height:3993px;overflow:hidden}
body{position:relative;font-family:'Poppins',sans-serif;color:var(--ink);background:var(--white)}
.abs{position:absolute}
.brand-name{font-family:'Poppins',sans-serif;font-weight:700;color:var(--blue);font-size:25px;line-height:1;white-space:nowrap}
.brand-mark{display:inline-block;width:22px;height:22px;background:var(--red);vertical-align:middle;margin-right:10px;flex:none}

/* header */
.header-top{top:0;left:0;width:1200px;height:88px;border-bottom:1px solid var(--line)}
.logo{left:144px;top:30px;display:flex;align-items:center}
.search{left:497px;top:25px;width:255px;height:38px;border:1px solid #ccc;border-radius:2px;font-size:13px;padding:10px 18px;color:#333}
.search svg{position:absolute;right:16px;top:10px}
.fav{left:783px;top:31px;font-size:14px;font-weight:500;display:flex;align-items:center;gap:10px}
.cart{left:950px;top:31px;font-size:14px;font-weight:500;display:flex;align-items:center;gap:8px}
.nav{top:102px;left:143px;display:flex;height:44px;align-items:center;font-size:14px;font-weight:500}
.nav a{color:var(--ink);text-decoration:none;padding:0 19px;border-right:1px solid var(--line);line-height:34px}
.nav a:first-child{padding-left:0;color:var(--red);text-decoration:underline;text-underline-offset:4px}
.nav a:last-child{border:none}
.btn{display:flex;align-items:center;justify-content:center;font-weight:700;font-size:14px;text-transform:uppercase;letter-spacing:.2px;background:var(--red);color:#fff}
.btn-contact{left:915px;top:102px;width:141px;height:44px}

/* hero */
.hero{top:166px;left:0;width:1200px;height:734px;overflow:hidden}
.hero-photo{position:absolute;inset:0;background:linear-gradient(160deg,#5b86cf 0%,#3a6bbd 45%,#2a5cae 100%)}
.hero-icon{left:551px;top:395px;width:98px;height:48px;border:3px solid #fff;border-radius:50%}
.hero-title{top:450px;left:0;width:1200px;text-align:center;font-size:45px;font-weight:800;line-height:53px;color:var(--red);-webkit-text-stroke:2px #fff;text-transform:uppercase}
.hero-sub{top:562px;left:200px;width:800px;text-align:center;font-size:23px;font-weight:600;line-height:33px;color:#fff}
.btn-shop{left:542px;top:642px;width:116px;height:48px;background:#fff;color:var(--red);border:3px solid var(--red);font-size:14px}

/* section headings */
.sec-title{left:0;width:1200px;text-align:center;font-size:40px;font-weight:700;color:var(--blue);text-transform:uppercase}
.divider{left:510px;width:180px;height:30px;display:flex;align-items:center;justify-content:space-between}
.divider span{display:block;width:56px;height:2px;background:var(--red)}
.divider i{display:block;width:54px;height:26px;border:3px solid var(--blue);border-radius:50%}
.divider.light span{background:#fff}
.divider.light i{border-color:#fff}

/* sports cards */
.sport{top:981px;width:285px;height:224px;display:flex;align-items:flex-end;justify-content:center;padding-bottom:20px;color:#fff;font-size:23px;font-weight:700;text-transform:uppercase}
.btn-design{left:508px;top:1247px;width:184px;height:43px}

/* locker room */
.locker{top:1367px;left:0;width:1200px;height:623px;background:linear-gradient(180deg,#d94a45,#d2403c)}
.card{width:213px;height:260px;background:#fff;border-radius:4px;text-align:center;font-size:14px}
.card .shirt{position:absolute;left:38px;top:36px;width:137px;height:137px;background:radial-gradient(circle,#3a2a24 0%,#111 55%,#fff 56%)}
.card .heart{position:absolute;right:16px;top:16px}
.card .name{position:absolute;top:193px;left:0;width:100%}
.card .price{position:absolute;top:217px;left:0;width:100%;font-weight:600}
.card .add{position:absolute;top:246px;left:0;width:100%;color:var(--red);font-weight:500;display:flex;justify-content:center;align-items:center;gap:10px}
.card .add u{text-underline-offset:3px}
.card.active{height:292px;border:2px solid var(--blue)}
.card.bordered{border:1px solid var(--line)}
.arrow{width:34px;height:34px;border-radius:50%;display:flex;align-items:center;justify-content:center}
.btn-white{background:#fff;color:var(--blue)}

/* uniforms */
.uni-blue{top:1990px;left:0;width:1200px;height:584px}
.uni-title{left:144px;top:2040px;font-size:40px;font-weight:700;color:var(--blue);line-height:48px}
.uni-icon{left:144px;top:2140px;width:56px;height:26px;border:3px solid var(--blue);border-radius:50%}
.uni-line{left:210px;top:2152px;width:56px;height:2px;background:var(--red)}
.uni-text{left:144px;top:2192px;width:460px;font-size:15.5px;line-height:25px;color:#333}
.uni-text p{margin-bottom:11px}
.uni-text h4{font-style:italic;font-weight:600;font-size:20px;margin:2px 0 10px}
.uni-text li{list-style:none;font-size:18px;line-height:35px;padding-left:26px;position:relative}
.uni-text li::before{content:"";position:absolute;left:0;top:16px;width:5px;height:5px;border-radius:50%;background:var(--red)}
.btn-uni{left:144px;top:2465px;width:248px;height:44px}
.ring{left:638px;top:2065px;width:440px;height:440px;border:2px solid #fff;border-radius:50%}
.ring2{left:652px;top:2079px;width:412px;height:412px;border:1px solid var(--blue);border-radius:50%}
.uni-photo{left:657px;top:2084px;width:402px;height:402px;border-radius:50%;background:linear-gradient(135deg,#7d6a5f,#b9602e 45%,#c9b6a4)}

/* brands */
.brands{top:2574px;left:0;width:1200px;height:366px;background:var(--grey)}
.brand-box{top:2772px;width:208px;height:88px;background:#fff;border-radius:4px;box-shadow:0 3px 10px rgba(0,0,0,.12);display:flex;align-items:center;justify-content:center;font-size:20px;font-weight:600;color:#555}

/* footer */
.footer{top:3500px;left:0;width:1200px;height:493px}
.foot-logo{left:144px;top:3814px;display:flex;align-items:center}
.foot-logo .brand-name{color:#fff;font-size:19px}
.foot-logo .brand-mark{width:18px;height:18px;margin-right:9px}
.foot-col{color:#fff;font-size:12.5px}
.foot-col h5{font-size:15px;font-weight:600;margin-bottom:14px;text-transform:uppercase}
.foot-col li{list-style:none;line-height:25.5px}
.contact-row{display:flex;gap:14px;align-items:flex-start;margin-bottom:18px;line-height:18px}
.contact-row i{flex:none;width:24px;height:24px;border-radius:50%;background:#fff;display:flex;align-items:center;justify-content:center}
.email{width:220px;height:35px;background:#fff;border-radius:18px;display:flex;align-items:center;justify-content:space-between;padding-left:14px;color:#777;font-size:10px}
.email b{width:44px;height:35px;background:var(--red);border-radius:0 18px 18px 0;display:flex;align-items:center;justify-content:center}
.social{display:flex;gap:8px;margin-top:14px}
.social span{width:24px;height:24px;border-radius:50%;background:#fff}
.social span:last-child{background:var(--red)}
.copyright{top:3941px;left:0;width:1200px;height:52px;background:var(--blue-dark);color:#fff;font-size:12px;display:flex;align-items:center;justify-content:center}
</style>
</head>
<body>

<!-- header -->
<header>
  <div class="abs header-top"></div>
  <div class="abs logo"><span class="brand-mark"></span><span class="brand-name">Rivet Athletic Supply</span></div>
  <div class="abs search">Search
    <svg width="18" height="18" viewBox="0 0 24 24" fill="none" stroke="#d63d3a" stroke-width="2.4"><circle cx="10" cy="10" r="7"/><path d="M15.5 15.5L21 21"/></svg>
  </div>
  <div class="abs fav">
    <svg width="24" height="22" viewBox="0 0 24 22" fill="none" stroke="#d63d3a" stroke-width="2"><path d="M12 20S2 13.5 2 7a5 5 0 0 1 10-1 5 5 0 0 1 10 1c0 6.5-10 13-10 13z"/></svg>Favourites</div>
  <div class="abs cart">
    <svg width="22" height="24" viewBox="0 0 22 24" fill="none" stroke="#d63d3a" stroke-width="2"><rect x="3" y="7" width="16" height="15" rx="2"/><path d="M7 9V5a4 4 0 0 1 8 0v4"/><circle cx="8" cy="19" r="4" fill="#2a5cae" stroke="none"/></svg>My Cart
    <svg width="10" height="10" viewBox="0 0 10 10" fill="none" stroke="#333" stroke-width="1.5"><path d="M2 3l3 3 3-3"/></svg></div>
  <nav class="abs nav">
    <a href="#">Home</a><a href="#">Locker Room</a><a href="#">Custom Uniforms</a><a href="#">Custom Shirt Creator</a><a href="#">Brands</a><a href="#">About</a>
  </nav>
  <a class="abs btn btn-contact">Contact Us</a>
</header>

<!-- hero -->
<section class="abs hero">
  <div class="hero-photo" role="img" aria-label="Two cheering female volleyball players, blue-toned photo"></div>
  <svg class="abs" style="left:0;top:0" width="1200" height="734" viewBox="0 0 1200 734">
    <polygon points="0,696 852,534 1200,731 1200,734 0,734" fill="#fff"/>
    <polygon points="852,534 1200,471 1200,731" fill="#d63d3a"/>
  </svg>
</section>
<div class="abs hero-icon"></div>
<h1 class="abs hero-title">Custom Sports Apparel<br>Built for the Game</h1>
<p class="abs hero-sub">Premium custom uniforms and fan gear for basketball, football, and baseball — designed by you, built to perform.</p>
<a class="abs btn btn-shop">Shop All</a>

<!-- sports -->
<h2 class="abs sec-title" style="top:858px">Sports We Serve</h2>
<div class="abs divider" style="top:915px"><span></span><i></i><span></span></div>
<div class="abs sport" style="left:144px;background:linear-gradient(180deg,#3d4f6b,#1c1f2a)" role="img" aria-label="Basketball players at the hoop">Basketball</div>
<div class="abs sport" style="left:458px;background:linear-gradient(180deg,#6b5a4e,#2a2522)" role="img" aria-label="Football players charging">Football</div>
<div class="abs sport" style="left:771px;background:linear-gradient(180deg,#3a2b2b,#1a1414)" role="img" aria-label="Baseball batter swinging">Baseball</div>
<a class="abs btn btn-design">Design Your Gear</a>

<!-- locker room -->
<section class="abs locker" role="img" aria-label="Red-toned background photo of athletes"></section>
<h2 class="abs sec-title" style="top:1425px;color:#fff">Our Locker Room</h2>
<div class="abs divider light" style="top:1480px"><span></span><i></i><span></span></div>
<div class="abs arrow" style="left:68px;top:1658px;background:#fff"><svg width="16" height="10" viewBox="0 0 16 10" fill="none" stroke="#2a5cae" stroke-width="2"><path d="M15 5H2M5 1L1 5l4 4"/></svg></div>
<div class="abs arrow" style="left:1098px;top:1658px;background:#fff"><svg width="16" height="10" viewBox="0 0 16 10" fill="none" stroke="#2a5cae" stroke-width="2"><path d="M1 5h13M11 1l4 4-4 4"/></svg></div>

<div class="abs card" style="left:144px;top:1545px"><div class="shirt" role="img" aria-label="Black t-shirt with basketball print"></div><svg class="heart" width="14" height="13" viewBox="0 0 24 22" fill="none" stroke="#d63d3a" stroke-width="2.4"><path d="M12 20S2 13.5 2 7a5 5 0 0 1 10-1 5 5 0 0 1 10 1c0 6.5-10 13-10 13z"/></svg><div class="name">Lorem ipsum dolor sit</div><div class="price">$399.95</div></div>
<div class="abs card" style="left:377px;top:1545px"><div class="shirt" role="img" aria-label="Black t-shirt with basketball print"></div><svg class="heart" width="14" height="13" viewBox="0 0 24 22" fill="none" stroke="#d63d3a" stroke-width="2.4"><path d="M12 20S2 13.5 2 7a5 5 0 0 1 10-1 5 5 0 0 1 10 1c0 6.5-10 13-10 13z"/></svg><div class="name">Lorem ipsum dolor sit</div><div class="price">$399.95</div></div>
<div class="abs card active" style="left:610px;top:1545px"><div class="shirt" role="img" aria-label="Black t-shirt with basketball print"></div><svg class="heart" width="14" height="13" viewBox="0 0 24 22" fill="none" stroke="#d63d3a" stroke-width="2.4"><path d="M12 20S2 13.5 2 7a5 5 0 0 1 10-1 5 5 0 0 1 10 1c0 6.5-10 13-10 13z"/></svg><div class="name">Lorem ipsum dolor sit</div><div class="price">$399.95</div><div class="add"><svg width="20" height="16" viewBox="0 0 20 16" fill="none" stroke="#d63d3a" stroke-width="1.6"><path d="M1 1h3l2 10h11l2-7H5"/><circle cx="8" cy="14" r="1.3"/><circle cx="16" cy="14" r="1.3"/></svg><u>ADD TO CART</u></div></div>
<div class="abs card" style="left:843px;top:1545px"><div class="shirt" role="img" aria-label="Black t-shirt with basketball print"></div><svg class="heart" width="14" height="13" viewBox="0 0 24 22" fill="none" stroke="#d63d3a" stroke-width="2.4"><path d="M12 20S2 13.5 2 7a5 5 0 0 1 10-1 5 5 0 0 1 10 1c0 6.5-10 13-10 13z"/></svg><div class="name">Lorem ipsum dolor sit</div><div class="price">$399.95</div></div>
<a class="abs btn btn-white" style="left:508px;top:1877px;width:184px;height:43px">View All Products</a>

<!-- custom uniforms -->
<svg class="abs uni-blue" width="1200" height="584" viewBox="0 0 1200 584"><polygon points="1023,0 1200,0 1200,584 649,584" fill="#2a5cae"/></svg>
<h2 class="abs uni-title">CUSTOM TEAM<br>UNIFORMS</h2>
<div class="abs uni-icon"></div><div class="abs uni-line"></div>
<div class="abs uni-text">
  <p>Built for performance. Designed for identity.</p>
  <p>Our uniforms are engineered for durability, comfort, and peak athletic performance. Choose from a wide range of styles, fabrics, and colorways</p>
  <h4>Available For</h4>
  <ul><li>Basketball uniforms</li><li>Football jerseys &amp; practice gear</li><li>Baseball jerseys &amp; pants</li></ul>
</div>
<a class="abs btn btn-uni">Explore Custom Uniforms</a>
<div class="abs ring"></div><div class="abs ring2"></div>
<div class="abs uni-photo" role="img" aria-label="Women's basketball game, player driving with the ball"></div>
<div class="abs" style="left:740px;top:2084px;width:9px;height:9px;border-radius:50%;background:var(--blue)"></div>
<div class="abs" style="left:969px;top:2460px;width:9px;height:9px;border-radius:50%;background:#fff"></div>

<!-- brands -->
<section class="abs brands"></section>
<h2 class="abs sec-title" style="top:2643px">Our Brands</h2>
<div class="abs divider" style="top:2698px"><span></span><i></i><span></span></div>
<div class="abs brand-box" style="left:144px">Northline</div>
<div class="abs brand-box" style="left:378px">Fieldhouse</div>
<div class="abs brand-box" style="left:613px">Courtline</div>
<div class="abs brand-box" style="left:848px">Ridgeway</div>

<!-- shirt creator -->
<h2 class="abs sec-title" style="top:3038px">Custom Shirt Creator</h2>
<div class="abs divider" style="top:3093px"><span></span><i></i><span></span></div>
<div class="abs arrow" style="left:68px;top:3270px;background:#dfe7f5"><svg width="16" height="10" viewBox="0 0 16 10" fill="none" stroke="#2a5cae" stroke-width="2"><path d="M15 5H2M5 1L1 5l4 4"/></svg></div>
<div class="abs arrow" style="left:1098px;top:3270px;background:var(--red)"><svg width="16" height="10" viewBox="0 0 16 10" fill="none" stroke="#fff" stroke-width="2"><path d="M1 5h13M11 1l4 4-4 4"/></svg></div>

<div class="abs card bordered" style="left:144px;top:3157px"><div class="shirt" role="img" aria-label="Black t-shirt with basketball print"></div><svg class="heart" width="14" height="13" viewBox="0 0 24 22" fill="none" stroke="#d63d3a" stroke-width="2.4"><path d="M12 20S2 13.5 2 7a5 5 0 0 1 10-1 5 5 0 0 1 10 1c0 6.5-10 13-10 13z"/></svg><div class="name">Lorem ipsum dolor sit</div><div class="price">$399.95</div></div>
<div class="abs card bordered" style="left:377px;top:3157px"><div class="shirt" role="img" aria-label="Black t-shirt with basketball print"></div><svg class="heart" width="14" height="13" viewBox="0 0 24 22" fill="none" stroke="#d63d3a" stroke-width="2.4"><path d="M12 20S2 13.5 2 7a5 5 0 0 1 10-1 5 5 0 0 1 10 1c0 6.5-10 13-10 13z"/></svg><div class="name">Lorem ipsum dolor sit</div><div class="price">$399.95</div></div>
<div class="abs card active" style="left:610px;top:3157px"><div class="shirt" role="img" aria-label="Black t-shirt with basketball print"></div><svg class="heart" width="14" height="13" viewBox="0 0 24 22" fill="none" stroke="#d63d3a" stroke-width="2.4"><path d="M12 20S2 13.5 2 7a5 5 0 0 1 10-1 5 5 0 0 1 10 1c0 6.5-10 13-10 13z"/></svg><div class="name">Lorem ipsum dolor sit</div><div class="price">$399.95</div><div class="add"><svg width="20" height="16" viewBox="0 0 20 16" fill="none" stroke="#d63d3a" stroke-width="1.6"><path d="M1 1h3l2 10h11l2-7H5"/><circle cx="8" cy="14" r="1.3"/><circle cx="16" cy="14" r="1.3"/></svg><u>ADD TO CART</u></div></div>
<div class="abs card bordered" style="left:843px;top:3157px"><div class="shirt" role="img" aria-label="Black t-shirt with basketball print"></div><svg class="heart" width="14" height="13" viewBox="0 0 24 22" fill="none" stroke="#d63d3a" stroke-width="2.4"><path d="M12 20S2 13.5 2 7a5 5 0 0 1 10-1 5 5 0 0 1 10 1c0 6.5-10 13-10 13z"/></svg><div class="name">Lorem ipsum dolor sit</div><div class="price">$399.95</div></div>

<!-- footer -->
<svg class="abs footer" width="1200" height="493" viewBox="0 0 1200 493">
  <polygon points="0,18 600,165 0,240" fill="#d63d3a"/>
  <polygon points="0,240 600,165 1200,18 1200,493 0,493" fill="#2a5cae"/>
</svg>
<a class="abs btn" style="left:508px;top:3487px;width:184px;height:43px;z-index:2">View All Products</a>
<div class="abs foot-logo"><span class="brand-mark" style="background:#fff"></span><span class="brand-name">Rivet Athletic Supply</span></div>
<div class="abs foot-col" style="left:434px;top:3718px">
  <h5>Site Map</h5>
  <ul><li>Home</li><li>Locker Room</li><li>Custom Uniforms</li><li>Custom Shirt Creator</li><li>Brands</li><li>About</li><li>Contact Us</li></ul>
</div>
<div class="abs foot-col" style="left:602px;top:3718px;width:220px">
  <h5>Contact Info</h5>
  <div class="contact-row"><i><svg width="12" height="12" viewBox="0 0 24 24" fill="#d63d3a"><path d="M6.6 10.8a15 15 0 0 0 6.6 6.6l2.2-2.2a1 1 0 0 1 1-.25 11 11 0 0 0 3.6.6 1 1 0 0 1 1 1V20a1 1 0 0 1-1 1A17 17 0 0 1 3 4a1 1 0 0 1 1-1h3.5a1 1 0 0 1 1 1 11 11 0 0 0 .6 3.6 1 1 0 0 1-.25 1z"/></svg></i>+1 555 010 2480</div>
  <div class="contact-row"><i><svg width="12" height="10" viewBox="0 0 24 18" fill="#d63d3a"><path d="M0 0h24v18H0zM2 2l10 8 10-8"/></svg></i>contact@rivet.example</div>
  <div class="contact-row"><i><svg width="10" height="13" viewBox="0 0 20 26" fill="#d63d3a"><path d="M10 0a10 10 0 0 0-10 10c0 7 10 16 10 16s10-9 10-16A10 10 0 0 0 10 0zm0 14a4 4 0 1 1 0-8 4 4 0 0 1 0 8z"/></svg></i>123, Rivet Athletic Supply Inc., USA</div>
</div>
<div class="abs foot-col" style="left:835px;top:3718px">
  <h5>Subscribe</h5>
  <div class="email">&#9993;&nbsp; Email Address <b><svg width="16" height="16" viewBox="0 0 24 24" fill="#fff"><path d="M2 11L22 2l-9 20-2-8z"/></svg></b></div>
  <div class="social" aria-label="Social media links"><span></span><span></span><span></span></div>
</div>
<div class="abs copyright">© 2025 &nbsp; / &nbsp; All Rights Reserved</div>

</body>
</html>
```